Business card and stationary for a consultant firm
Sharp Compass
Professional
Renske Hoorneman
Zwaluwlaan 38
Curaçao
Renskehoorneman@postvlek.com
Zwaluwlaan38

```html
<!DOCTYPE html>
<html lang="en">
<head>
<meta charset="utf-8">
<title>Sharp Compass – Business Card</title>
<link href="https://fonts.googleapis.com/css2?family=Cormorant+Garamond:ital,wght@0,400;0,500;0,600;1,400&display=swap" rel="stylesheet">
<style>
  :root {
    --page-bg: #ecebe6;
    --frame: #b2b23a;
    --frame-dark: #9f9f2e;
    --paper: #ffffff;
    --paper-shade: #efefef;
    --ink: #2b2b2b;
    --ink-soft: #555555;
    --accent: #e08a1e;
    --rule: #9a9a9a;
  }
  * { margin: 0; padding: 0; box-sizing: border-box; }
  html, body {
    width: 1200px;
    height: 914px;
    overflow: hidden;
    background: var(--page-bg);
  }
  .card {
    position: absolute;
    left: 110px;
    top: 177px;
    width: 980px;
    height: 560px;
    background: var(--frame);
    box-shadow: 0 10px 30px rgba(0,0,0,0.18);
    padding: 36px;
  }
  .card-face {
    position: relative;
    width: 100%;
    height: 100%;
    background: radial-gradient(ellipse at 55% 45%, var(--paper) 55%, var(--paper-shade) 100%);
    box-shadow: inset 0 0 0 1px var(--frame-dark);
    font-family: "Cormorant Garamond", Georgia, serif;
    color: var(--ink);
  }
  .divider {
    position: absolute;
    left: 420px;
    top: 92px;
    width: 1px;
    height: 268px;
    background: var(--rule);
  }
  .brand-mark {
    position: absolute;
    left: 318px;
    top: 100px;
    width: 78px;
    height: 78px;
    border-radius: 50%;
    background: var(--accent);
  }
  .brand-name {
    position: absolute;
    left: 438px;
    top: 110px;
    font-size: 62px;
    font-weight: 600;
    letter-spacing: 0.5px;
    color: var(--ink);
    line-height: 1;
  }
  .holder {
    position: absolute;
    right: 508px;
    top: 232px;
    text-align: right;
    font-variant: small-caps;
  }
  .holder-name {
    font-size: 26px;
    font-weight: 500;
    color: var(--accent);
    letter-spacing: 1px;
  }
  .holder-address {
    margin-top: 10px;
    font-size: 23px;
    color: var(--ink-soft);
    letter-spacing: 0.6px;
  }
  .contacts {
    position: absolute;
    left: 436px;
    top: 258px;
    list-style: none;
    font-size: 20px;
    color: var(--ink-soft);
    font-variant: small-caps;
    letter-spacing: 0.6px;
  }
  .contacts li {
    display: flex;
    align-items: center;
    gap: 10px;
    height: 30px;
  }
  .contacts svg { width: 16px; height: 16px; flex: none; }
</style>
</head>
<body>
  <div class="card">
    <div class="card-face">
      <div class="brand-mark"></div>
      <div class="divider"></div>
      <div class="brand-name">sharpcompass</div>

      <div class="holder">
        <div class="holder-name">Renske Hoorneman</div>
        <div class="holder-address">Zwaluwlaan 38 Curaçao</div>
      </div>

      <ul class="contacts">
        <li>
          <svg viewBox="0 0 16 16"><rect width="16" height="16" rx="2" fill="#e08a1e"/><path d="M5 3.5c.6 0 1 .9 1.3 1.6.2.5-.5.9-.7 1.2.5 1.4 1.6 2.5 3 3 .3-.2.7-.9 1.2-.7.7.3 1.6.7 1.6 1.3 0 .9-.9 1.6-1.8 1.6C6.6 11.5 4.5 9.4 4 6 3.9 4.5 4.2 3.5 5 3.5z" fill="#fff"/></svg>
          <span>(599 9) 555 0142</span>
        </li>
        <li>
          <svg viewBox="0 0 16 16"><rect width="16" height="16" rx="2" fill="#e08a1e"/><rect x="3" y="4.5" width="10" height="7" fill="none" stroke="#fff" stroke-width="1.2"/><path d="M3 4.5l5 4 5-4" fill="none" stroke="#fff" stroke-width="1.2"/></svg>
          <span>Renskehoorneman@postvlek.com</span>
        </li>
        <li>
          <svg viewBox="0 0 16 16"><rect width="16" height="16" rx="2" fill="#e08a1e"/><circle cx="8" cy="8" r="4.8" fill="none" stroke="#fff" stroke-width="1.1"/><ellipse cx="8" cy="8" rx="2" ry="4.8" fill="none" stroke="#fff" stroke-width="1"/><path d="M3.2 8h9.6" stroke="#fff" stroke-width="1"/></svg>
          <span>www.Zwaluwlaan38.com</span>
        </li>
      </ul>
    </div>
  </div>
</body>
</html>
```